Velmora - New coded website

Current website is around 5 years old and corrupted in some ways...
I would like to refresh the design and to create a new coded website based on the current content .
Please refer to :
www.velmora-sample.com.au

Coded - Design and coding required

```html
<!DOCTYPE html>
<html lang="en">
<head>
<meta charset="utf-8">
<title>Velmora — Odours Controlled Naturally</title>
<link href="https://fonts.googleapis.com/css2?family=Poppins:wght@500;600;700&family=Inter:wght@400;500;600&display=swap" rel="stylesheet">
<style>
:root{
  --green:#6cb33f;
  --green-soft:#eef6e6;
  --green-pale:#dcedcf;
  --navy:#0d2b36;
  --teal:#0a4d6b;
  --teal-dark:#0c2430;
  --text:#23323a;
  --muted:#5d6a70;
  --line:#cfe4bf;
  --white:#fff;
}
*{box-sizing:border-box;margin:0;padding:0}
html,body{width:1200px;height:2633px;overflow:hidden}
body{position:relative;font-family:"Inter",sans-serif;color:var(--text);background:var(--white)}
.abs{position:absolute}
h1,h2,h3{font-family:"Poppins",sans-serif}

/* top bar */
.topbar{left:0;top:0;width:1200px;height:32px;background:#000;color:#fff;font-size:12px}
.topbar .contact{left:160px;top:9px;display:flex;gap:20px}
.topbar .contact span{display:flex;align-items:center;gap:6px}
.topbar .quote{left:904px;top:0;width:136px;height:32px;background:var(--green);color:#fff;font-weight:600;font-size:11.5px;display:flex;align-items:center;justify-content:center}

/* hero */
.hero-bg{left:0;top:32px;width:1200px;height:490px}
.brand{left:158px;top:50px;display:flex;align-items:center;gap:10px}
.brand .mark{width:52px;height:52px;border-radius:50%;background:var(--green)}
.brand .name{font-size:28px;font-weight:500;color:var(--teal)}
.nav{left:394px;top:69px;display:flex;gap:13px;font-size:12px;color:var(--navy)}
.hero-title{left:158px;top:176px;font-weight:700;line-height:1}
.hero-title .l1{font-size:74px;color:var(--navy);display:block}
.hero-title .l2{font-size:56px;color:var(--navy);display:block;margin-top:10px}
.hero-title .l3{font-size:62px;color:var(--green);display:block;margin-top:8px}
.btn{border-radius:20px;font-size:11.5px;font-weight:600;display:flex;align-items:center;justify-content:center}
.btn-green{background:var(--green);color:#fff}
.btn-white{background:#fff;color:var(--teal)}
.hero-btn{left:160px;top:398px;width:134px;height:36px}
.hero-photo{left:560px;top:131px;width:356px;height:356px;border-radius:50%;background:radial-gradient(circle at 45% 40%,#d9685f 0%,#c94a4f 25%,#8fa36a 60%,#5e7a45 100%)}

/* feature cards */
.card{width:129px;height:145px;border:1.5px solid var(--line);border-radius:14px;background:#fff;display:flex;flex-direction:column;align-items:center;justify-content:flex-end;padding-bottom:16px;gap:18px;font-family:"Poppins",sans-serif;font-weight:600;font-size:13px;color:var(--green)}
.card.active{background:var(--green);border-color:var(--green);color:#fff;box-shadow:0 8px 18px rgba(0,0,0,.12)}
.side-shape{left:1010px;top:560px;width:190px;height:500px}

.video{left:161px;top:793px;width:493px;height:277px;border-radius:14px;background:linear-gradient(180deg,#d9efc9 0%,#cbe8b3 60%,#e6f3dc 100%)}
.video .play{position:absolute;left:222px;top:116px;width:50px;height:50px;border-radius:50%;background:#fff;box-shadow:0 2px 8px rgba(0,0,0,.15)}
.best-title{left:686px;top:770px;font-size:25px;font-weight:600;color:var(--teal)}
.best{left:686px;width:205px;height:56px;background:#fff;border-radius:6px;box-shadow:0 3px 14px rgba(0,0,0,.08);display:flex;align-items:center;gap:7px;padding:0 12px;font-size:11px;color:var(--navy);white-space:nowrap}

/* about */
.about{left:0;top:1151px;width:1200px;height:286px;background:var(--teal);color:#fff;text-align:center}
.about .kicker{position:absolute;left:0;width:1200px;top:50px;font-size:14px;font-weight:500}
.about h2{position:absolute;left:0;width:1200px;top:70px;font-size:25px;font-weight:600}
.about p{position:absolute;left:250px;width:700px;top:118px;font-size:11.3px;line-height:15px}
.about p em{font-style:normal;color:var(--green)}
.about .b1{left:476px;top:200px;width:136px;height:36px}
.about .b2{left:624px;top:200px;width:100px;height:36px}

/* testimonial */
.t-title{left:0;width:1200px;top:1492px;text-align:center;font-size:25px;font-weight:600;color:var(--teal)}
.t-card{left:281px;top:1545px;width:647px;height:213px;background:#fff;border-radius:14px;box-shadow:0 4px 26px rgba(0,0,0,.08);padding:34px 38px}
.t-card .who{font-family:"Poppins",sans-serif;font-size:14px;font-weight:600;color:var(--green)}
.t-card .role{font-size:10.5px;color:var(--navy);margin-top:2px}
.t-card h3{font-family:"Inter",sans-serif;font-size:14px;font-weight:600;color:var(--teal);margin-top:8px}
.t-card blockquote{font-size:9.8px;font-style:italic;color:var(--muted);line-height:15px;margin-top:14px}

/* clients */
.clients-title{left:160px;top:1845px;font-size:25px;font-weight:600;color:var(--teal);line-height:1.3}
.arrow{width:38px;height:38px;border-radius:50%;background:var(--green)}
.client{top:1871px;font-family:"Poppins",sans-serif;font-weight:600;font-size:16px;color:#3c4a52;display:flex;align-items:center;gap:8px;white-space:nowrap}
.client i{display:inline-block;width:20px;height:20px;border-radius:50%;background:#9aa8ae}

/* contact */
.contact-strip{left:0;top:1943px;width:66px;height:422px;background:var(--green)}
.c-title{left:160px;top:2000px;font-size:25px;font-weight:600;color:var(--teal)}
.c-sub{left:160px;top:2051px;width:400px;font-size:11px;line-height:15px;color:var(--navy)}
.field{border:1px solid var(--line);border-radius:4px;font-size:11px;color:#8a969b;padding:12px 11px;background:#fff}
.map{left:684px;top:1943px;width:516px;height:422px;background:linear-gradient(160deg,#dbe8f0,#cfdfe9 60%,#e1ebf1)}

/* footer */
.footer{left:0;top:2365px;width:1200px;height:237px;background:var(--teal-dark);color:#fff}
.f-head{top:2418px;font-size:15px;font-weight:600;color:#fff}
.f-list{left:313px;top:2456px;font-size:10.5px;line-height:22.5px;text-transform:uppercase;color:#fff}
.f-addr{left:534px;top:2456px;font-size:11px;line-height:16px;color:#fff}
.f-sub{left:760px;top:2450px;width:210px;font-size:9px;line-height:12px;color:#fff}
.f-sub strong{font-size:11px;display:block;margin-bottom:8px}
.f-input{left:760px;top:2506px;width:206px;height:34px;border-radius:17px;background:#fff;color:#333;font-size:10px;display:flex;align-items:center;padding-left:12px}
.f-input .go{position:absolute;right:0;top:0;width:74px;height:34px;border-radius:17px;background:var(--green);color:#fff;display:flex;align-items:center;justify-content:center;font-size:10.5px}
.f-vert{left:988px;top:2420px;writing-mode:vertical-rl;font-size:24px;font-weight:500;color:#fff}
.bottom{left:0;top:2602px;width:1200px;height:31px;background:var(--teal);color:#fff;font-size:10px}
</style>
</head>
<body>

<div class="abs topbar">
  <div class="abs contact">
    <span><svg width="10" height="10" viewBox="0 0 24 24"><path fill="#6cb33f" d="M6.6 10.8a15 15 0 0 0 6.6 6.6l2.2-2.2c.3-.3.7-.4 1-.2 1.1.4 2.3.6 3.6.6.6 0 1 .4 1 1V20c0 .6-.4 1-1 1A17 17 0 0 1 3 4c0-.6.4-1 1-1h3.5c.6 0 1 .4 1 1 0 1.3.2 2.5.6 3.6.1.3 0 .7-.2 1z"/></svg>+61 (08) 5550 0142</span>
    <span><svg width="12" height="10" viewBox="0 0 24 18"><rect width="24" height="18" rx="2" fill="#6cb33f"/><path d="M1 2l11 8 11-8" stroke="#000" stroke-width="2" fill="none"/></svg>Email Us</span>
  </div>
  <div class="abs quote">REQUEST A QUOTE</div>
</div>

<svg class="abs hero-bg" viewBox="0 0 1200 490" preserveAspectRatio="none" aria-hidden="true">
  <path d="M0 0H1200V330C1080 300 980 330 860 390 720 460 600 440 440 470 260 505 120 480 0 415Z" fill="var(--green-soft)"/>
</svg>

<div class="abs brand"><span class="mark"></span><span class="name">Velmora</span></div>
<nav class="abs nav">
  <span>Odour Control Products ⌄</span><span>How Biofiltration Works ⌄</span><span>Odour Control by Industry ⌄</span><span>Past Projects</span><span>About Us</span><span>Contact</span>
</nav>

<h1 class="abs hero-title"><span class="l1">Odours</span><span class="l2">Controlled</span><span class="l3">Naturally</span></h1>
<div class="abs btn btn-green hero-btn">REQUEST A QUOTE</div>
<div class="abs hero-photo" role="img" aria-label="Photo of a woman breathing fresh air with arms outstretched in a park"></div>

<svg class="abs side-shape" viewBox="0 0 190 500" aria-hidden="true">
  <circle cx="250" cy="250" r="250" fill="var(--green-pale)"/>
</svg>

<div class="abs card" style="left:386px;top:567px">
  <svg width="66" height="42" viewBox="0 0 66 42" aria-hidden="true"><circle cx="9" cy="6" r="5" fill="#111"/><path d="M2 14h12l8 6h6v4h-8l-4-3v19H3z" fill="#111"/><rect x="26" y="4" width="38" height="32" fill="none" stroke="#111" stroke-width="3"/><path d="M37 12l8-4 8 4v10l-8 4-8-4z" fill="none" stroke="#111" stroke-width="2.5"/></svg>
  PRODUCTS</div>
<div class="abs card active" style="left:535px;top:567px">
  <svg width="62" height="52" viewBox="0 0 62 52" aria-hidden="true"><path d="M16 4h40l-8 40H8z" fill="none" stroke="#fff" stroke-width="4"/><path d="M22 14h26M20 22h24M18 30h22" stroke="#fff" stroke-width="3"/><path d="M2 40c10 2 20 8 30 8" stroke="#fff" stroke-width="4" fill="none"/></svg>
  FEATURES</div>
<div class="abs card" style="left:685px;top:567px">
  <svg width="58" height="52" viewBox="0 0 58 52" aria-hidden="true"><circle cx="29" cy="26" r="17" fill="none" stroke="#111" stroke-width="5"/><path d="M6 40l14-14 8 8 22-24" stroke="#111" stroke-width="5" fill="none"/><path d="M40 6h12v12" stroke="#111" stroke-width="5" fill="none"/></svg>
  PAST PROJECTS</div>

<div class="abs video" role="img" aria-label="Illustration of biofilter tanks among green hills and trees, video thumbnail"><span class="play"><svg width="50" height="50" viewBox="0 0 50 50" aria-hidden="true"><path d="M20 16l14 9-14 9z" fill="var(--green)"/></svg></span></div>

<h2 class="abs best-title">What makes us the best?</h2>
<div class="abs best" style="top:822px"><svg width="30" height="28" viewBox="0 0 30 28" aria-hidden="true"><circle cx="16" cy="10" r="7" fill="none" stroke="#6cb33f" stroke-width="1.5"/><path d="M2 22h8l6 3 10-5" stroke="#6cb33f" stroke-width="1.5" fill="none"/></svg>Efficient maintenance cost</div>
<div class="abs best" style="top:892px"><svg width="34" height="28" viewBox="0 0 34 28" aria-hidden="true"><path d="M3 10l8-7 6 2 4-3 6 5 5 8-4 8-7 1-4-3-8 1-6-4z" fill="none" stroke="#6cb33f" stroke-width="1.5"/></svg>100% Australian Owned</div>
<div class="abs best" style="top:961px"><svg width="32" height="30" viewBox="0 0 32 30" aria-hidden="true"><circle cx="16" cy="15" r="12" fill="none" stroke="#6cb33f" stroke-width="1.5"/><path d="M10 12c4-6 10-4 12 0M9 19c3 4 9 5 13 1" stroke="#6cb33f" stroke-width="1.5" fill="none"/></svg>Eco Friendly</div>
<div class="abs best" style="top:1030px"><svg width="30" height="30" viewBox="0 0 30 30" aria-hidden="true"><circle cx="15" cy="15" r="6" fill="none" stroke="#6cb33f" stroke-width="1.5"/><path d="M15 2v5M15 23v5M2 15h5M23 15h5M6 6l3 3M21 21l3 3M24 6l-3 3M6 24l3-3" stroke="#6cb33f" stroke-width="1.5"/></svg><span>Biological &amp; Sustainable<br>technology</span></div>

<section class="abs about">
  <div class="kicker">Odour Control Solutions</div>
  <h2>About Velmora</h2>
  <p>Velmora uses sustainable biotechnology to resolve odour and <em>corrosion</em> problems in a highly efficient, environmentally friendly and cost-effective manner. Our, products, the VelVent series of biofilters have been specifically engineered to overcome issues traditionally associated with biofiltration, such as bed compaction and uneven moisture levels, and our patented design achieves a removal rate of up to 99.9% per stage of treatment.</p>
  <div class="abs btn btn-green b1">REQUEST A QUOTE</div>
  <div class="abs btn btn-white b2">READ MORE</div>
</section>

<h2 class="abs t-title">What people think about us</h2>
<article class="abs t-card">
  <div class="who">Sam Porter</div>
  <div class="role">Nearby resident to Elmwood Wastewater Pump Station</div>
  <h3>As soon as the system was started, the smell disappeared!</h3>
  <blockquote>"Mark and the Velmora team promised to stop the odour from our smelly neighbor and they delivered- in spades! As soon as the system was started, the smell disappeared. The system is well designed, very professionally installed and the beauty of it is, apart from a constantly running fan, it is bacteria doing the heavy lifting, so it is very environmentally friendly. We lived with the smell for 3 three years which could be extremely frustrating and unpleasant. Now, the problem is solved and we can have BBQs again. We are happy and our neighbours have noticed the odour is gone. Thank you!"</blockquote>
</article>

<h2 class="abs clients-title">Our happy<br>clients</h2>
<div class="abs arrow" style="left:386px;top:1864px"><svg width="38" height="38" viewBox="0 0 38 38" aria-hidden="true"><path d="M22 12l-7 7 7 7" stroke="#fff" stroke-width="2.5" fill="none"/></svg></div>
<div class="abs client" style="left:450px">Coastline Council</div>
<div class="abs client" style="left:640px"><i></i>Aqua Utility</div>
<div class="abs client" style="left:808px"><i></i>Territory Works</div>
<div class="abs arrow" style="left:987px;top:1864px"><svg width="38" height="38" viewBox="0 0 38 38" aria-hidden="true"><path d="M16 12l7 7-7 7" stroke="#fff" stroke-width="2.5" fill="none"/></svg></div>

<div class="abs contact-strip"></div>
<h2 class="abs c-title">Get in Contact</h2>
<p class="abs c-sub">If you have any queries regarding out products, please do not hesitate to contact us</p>
<div class="abs field" style="left:160px;top:2092px;width:206px;height:35px">First Name</div>
<div class="abs field" style="left:386px;top:2092px;width:206px;height:35px">Surname</div>
<div class="abs field" style="left:160px;top:2136px;width:206px;height:35px">Email</div>
<div class="abs field" style="left:386px;top:2136px;width:206px;height:35px">Phone</div>
<div class="abs field" style="left:160px;top:2181px;width:431px;height:74px">Message</div>
<div class="abs btn btn-green" style="left:160px;top:2266px;width:64px;height:36px">SEND</div>
<div class="abs map" role="img" aria-label="Street map showing the office location in an industrial area"><svg width="516" height="422" aria-hidden="true"><path d="M270 200c0-6 6-10 10-10s10 4 10 10c0 8-10 16-10 16s-10-8-10-16z" fill="#e53935"/></svg></div>

<footer class="abs footer"></footer>
<h3 class="abs f-head" style="left:313px">Quick Menu</h3>
<div class="abs f-list">› Odour Control Products<br>How Biofiltration Works<br>Odour Control by Industry<br>Past Projects<br>About Us</div>
<h3 class="abs f-head" style="left:534px">Address</h3>
<div class="abs f-addr">
  <div>☏ +61 (08) 5550 0142</div>
  <div style="margin-top:3px">⌖ 14 Harlow Crescent, Greenvale WA<br>6021, Australia</div>
  <div style="margin-top:12px;display:flex;align-items:center;gap:8px">Connect Us: <span style="display:inline-block;width:11px;height:11px;background:var(--green)"></span></div>
</div>
<h3 class="abs f-head" style="left:760px">Subscription</h3>
<div class="abs f-sub"><strong>Subscribe Us Now</strong>Lorem ipsum dolor sit amet, consectetur adipiscing elit, sed do eiusmod tempor</div>
<div class="abs f-input">Enter Your Email<span class="go">Subscribe</span></div>
<div class="abs f-vert">Velmora</div>

<div class="abs bottom">
  <span class="abs" style="left:160px;top:10px">Website by Studio Lumen</span>
  <span class="abs" style="left:806px;top:10px">Privacy Policy&nbsp;&nbsp; Sitemap&nbsp;&nbsp; ABN: 12 345 678 901</span>
</div>

</body>
</html>
```